Professional business cards for real estate development company

I need business cards for my new real estate development company. The company, "LUMAR" is a real estate development, investment, and advisory firm with a focus on multifamily, office, and mixed-use projects across primary and secondary markets in the Southeast United States.

Style preference is modern

Industry/Entity Type

Real Estate Development

Contact Information for Business Card

The business cards need to include:
Name
Title
Mailing Address
Phone Number
Web Address

Logo is attached. I would like white to be the primary color with incorporation of the company colors: #232D3A and #B5A451

Font styles to use
Other font styles liked:
• Montserrat, Avenir

Requirements
Must have
• Company Logo. No need to include the company name since the name is in the logo.
Should not have
• No line type designs

```html
<!DOCTYPE html>
<html lang="en">
<head>
<meta charset="utf-8">
<title>LUMAR Business Cards</title>
<link rel="stylesheet" href="https://fonts.googleapis.com/css2?family=Montserrat:wght@700&family=Ubuntu:wght@400;500&display=swap">
<style>
  :root {
    --stage: #212b38;
    --navy: #232d3a;
    --strip: #424a55;
    --gold: #b5a451;
    --white: #ffffff;
    --ink: #0f1115;
  }
  * { box-sizing: border-box; margin: 0; padding: 0; }
  html, body { width: 1200px; height: 1200px; overflow: hidden; }
  body { background: var(--stage); position: relative; font-family: "Ubuntu", sans-serif; }

  .card {
    position: absolute;
    left: 196px;
    width: 809px;
    height: 489px;
    background: var(--white);
    box-shadow: 0 22px 40px rgba(0, 0, 0, 0.45);
    overflow: hidden;
  }
  .card--front { top: 79px; }
  .card--back { top: 624px; }

  .brand {
    position: absolute;
    left: 0; right: 0;
    text-align: center;
    font-family: "Ubuntu", sans-serif;
    font-weight: 500;
    color: var(--navy);
    line-height: 1;
  }
  .card--front .brand { top: 110px; font-size: 52px; letter-spacing: 4px; }
  .card--back .brand { top: 190px; font-size: 120px; letter-spacing: 10px; }

  .holder {
    position: absolute;
    top: 237px; left: 0; right: 0;
    text-align: center;
  }
  .holder__name {
    font-family: "Montserrat", sans-serif;
    font-weight: 700;
    font-size: 38px;
    color: var(--ink);
    line-height: 1.1;
  }
  .holder__title {
    font-size: 30px;
    color: var(--navy);
    margin-top: 4px;
  }

  .contact-band {
    position: absolute;
    left: 0; right: 0; bottom: 0;
    height: 133px;
    background: var(--navy);
  }
  .contact-band__strip {
    position: absolute;
    top: 12px; left: 0; right: 0;
    height: 33px;
    background: var(--strip);
  }
  .contact {
    position: absolute;
    top: 11px;
    width: 260px;
    margin-left: -130px;
    text-align: center;
  }
  .contact--email { left: 160px; }
  .contact--phone { left: 398px; }
  .contact--web { left: 645px; }
  .contact__icon {
    display: block;
    width: 34px; height: 34px;
    margin: 0 auto;
  }
  .contact__text {
    display: block;
    margin-top: 10px;
    font-size: 16px;
    letter-spacing: 1.2px;
    color: var(--white);
  }
</style>
</head>
<body>

<section class="card card--front">
  <div class="brand">LUMAR</div>

  <div class="holder">
    <p class="holder__name">JANATHAN DOE</p>
    <p class="holder__title">Job Tittle Here</p>
  </div>

  <div class="contact-band">
    <div class="contact-band__strip"></div>

    <div class="contact contact--email">
      <svg class="contact__icon" viewBox="0 0 34 34" aria-hidden="true">
        <circle cx="17" cy="17" r="17" fill="var(--gold)"/>
        <path d="M10 10 L25 17 L10 23 L14 17 Z" fill="var(--white)"/>
      </svg>
      <span class="contact__text">BRAND-NAME@EMAIL.COM</span>
    </div>

    <div class="contact contact--phone">
      <svg class="contact__icon" viewBox="0 0 34 34" aria-hidden="true">
        <circle cx="17" cy="17" r="17" fill="var(--gold)"/>
        <path d="M9 14 Q17 9 25 14 L24 16 L20 15 L20 13 Q17 12 14 13 L14 15 L10 16 Z" fill="var(--white)"/>
        <rect x="11" y="17" width="12" height="7" rx="1.5" fill="var(--white)"/>
        <circle cx="17" cy="20.5" r="2" fill="var(--gold)"/>
      </svg>
      <span class="contact__text">+000 1234 5678 999</span>
    </div>

    <div class="contact contact--web">
      <svg class="contact__icon" viewBox="0 0 34 34" aria-hidden="true">
        <circle cx="17" cy="17" r="17" fill="var(--gold)"/>
        <circle cx="17" cy="17" r="8" fill="none" stroke="var(--white)" stroke-width="2"/>
        <ellipse cx="17" cy="17" rx="3.5" ry="8" fill="none" stroke="var(--white)" stroke-width="1.5"/>
        <line x1="9" y1="17" x2="25" y2="17" stroke="var(--white)" stroke-width="1.5"/>
      </svg>
      <span class="contact__text">WWW.BRANDNAME.COM</span>
    </div>
  </div>
</section>

<section class="card card--back">
  <div class="brand">LUMAR</div>
</section>

</body>
</html>
```